Scientific and medical consulting company needs "not a plain" business card.

I need a business card that looks different, or made differently, or functions as something. I am seeking to give it out at a medical device conference to get business and initial contacts. The final design should communicate medical competence, scientific know how, and creativity.

It needs to use my existing logo (created on Pixel Harbor!).
Each side should be something different., have different style.

Medical

```html
<!DOCTYPE html>
<html lang="en">
<head>
<meta charset="utf-8">
<title>Lumen Clinical – Business Card</title>
<link href="https://fonts.googleapis.com/css2?family=Open+Sans:wght@400;600;700&display=swap" rel="stylesheet">
<style>
  :root {
    --page: #e6e6e6;
    --white: #ffffff;
    --grey-band: #e4e4e4;
    --grey-box: #cfd0d1;
    --blue-light: #3aa8e6;
    --blue: #1a6fb0;
    --blue-deep: #0d4c8a;
    --navy: #1f4f8f;
    --green: #3b8b3f;
    --rule: #9a9a9a;
    --ink: #333333;
  }
  * { box-sizing: border-box; margin: 0; padding: 0; }
  html, body { width: 1200px; height: 1173px; overflow: hidden; }
  body {
    background: var(--page);
    font-family: "Open Sans", Arial, sans-serif;
    position: relative;
  }
  .card {
    position: absolute;
    top: 216px;
    width: 420px;
    height: 740px;
    box-shadow: 0 6px 18px rgba(0,0,0,0.18);
    overflow: hidden;
  }

  /* ---------- back side ---------- */
  .card-back { left: 150px; background: var(--white); }
  .back-url {
    position: absolute;
    left: 28px; top: 28px; width: 364px; height: 150px;
    background: var(--grey-box);
    border-radius: 0 44px 0 0;
    display: flex; align-items: center; justify-content: center;
    font-size: 21px; letter-spacing: 0.5px; color: var(--ink);
  }
  .back-panel {
    position: absolute;
    left: 28px; top: 196px; width: 364px; height: 516px;
    background: radial-gradient(circle at 45% 35%, var(--blue-light) 0%, var(--blue) 45%, var(--blue-deep) 100%);
    border-radius: 0 0 0 60px;
    padding: 54px 24px 0 30px;
  }
  .services { list-style: none; color: var(--white); }
  .services li { font-size: 17px; line-height: 1.35; margin-bottom: 22px; }

  /* ---------- front side ---------- */
  .card-front {
    left: 630px;
    background: linear-gradient(160deg, var(--blue) 0%, var(--blue-deep) 100%);
  }
  .front-panel {
    position: absolute;
    left: 24px; top: 28px; width: 372px; height: 684px;
    background: var(--white);
    border-radius: 54px 0 54px 0;
    overflow: hidden;
  }
  .brand {
    height: 130px;
    display: flex; align-items: center; justify-content: center; gap: 14px;
  }
  .brand-dot {
    width: 46px; height: 46px; border-radius: 50%;
    background: var(--blue);
  }
  .brand-name {
    font-size: 33px; font-weight: 700; color: var(--blue);
  }
  .contacts {
    background: var(--grey-band);
    height: 318px;
    padding: 26px 22px 0 30px;
    list-style: none;
  }
  .contact {
    display: flex; align-items: flex-start; gap: 18px;
    height: 70px;
  }
  .contact-icon { flex: 0 0 42px; width: 42px; height: 42px; }
  .contact-text {
    flex: 1;
    font-size: 15px; color: var(--ink); line-height: 1.3;
    border-bottom: 1.5px solid var(--rule);
    padding: 12px 0 10px 10px;
    margin-top: 0;
  }
  .contact:last-child .contact-text { border-bottom: none; padding-top: 6px; }
  .holder { text-align: center; padding-top: 56px; }
  .holder-name {
    font-size: 30px; font-weight: 700; letter-spacing: 1px; color: var(--navy);
  }
  .holder-role { font-size: 23px; color: var(--blue); margin-top: 2px; }
</style>
</head>
<body>

<section class="card card-back" aria-label="Card back">
  <div class="back-url">www.lumenclinical.com</div>
  <div class="back-panel">
    <ul class="services">
      <li>Expert opinion on new device design</li>
      <li>In vitro and in vivo correlation with scientific data</li>
      <li>Emergency Medicine specialist broad knowledge of multiple specialties</li>
      <li>Education, collaboration, publication</li>
    </ul>
  </div>
</section>

<section class="card card-front" aria-label="Card front">
  <div class="front-panel">
    <div class="brand">
      <span class="brand-dot"></span>
      <span class="brand-name">Lumen Clinical</span>
    </div>
    <ul class="contacts">
      <li class="contact">
        <svg class="contact-icon" viewBox="0 0 42 42" aria-hidden="true">
          <circle cx="21" cy="21" r="19" fill="#fff" stroke="var(--green)" stroke-width="2.5"/>
          <path d="M15 11c2 0 3 4 3 5s-2 2-2 3 4 6 6 6 2-2 3-2 5 1 5 3-2 5-5 4c-6-2-12-8-13-14 0-3 1-5 3-5z" fill="var(--green)"/>
        </svg>
        <span class="contact-text">+44 555 018 27</span>
      </li>
      <li class="contact">
        <svg class="contact-icon" viewBox="0 0 42 42" aria-hidden="true">
          <circle cx="21" cy="21" r="19" fill="#fff" stroke="var(--green)" stroke-width="2.5"/>
          <rect x="11" y="14" width="20" height="14" fill="var(--green)"/>
          <path d="M11 14l10 8 10-8" fill="none" stroke="#fff" stroke-width="1.6"/>
        </svg>
        <span class="contact-text">hello@lumenclinical.com</span>
      </li>
      <li class="contact">
        <svg class="contact-icon" viewBox="0 0 42 42" aria-hidden="true">
          <circle cx="21" cy="21" r="19" fill="#fff" stroke="var(--green)" stroke-width="2.5"/>
          <circle cx="21" cy="21" r="11" fill="var(--green)"/>
          <g fill="none" stroke="#fff" stroke-width="1.3">
            <ellipse cx="21" cy="21" rx="5" ry="11"/>
            <line x1="10" y1="21" x2="32" y2="21"/>
            <line x1="12" y1="15" x2="30" y2="15"/>
            <line x1="12" y1="27" x2="30" y2="27"/>
          </g>
        </svg>
        <span class="contact-text">www.lumenclinical.com</span>
      </li>
      <li class="contact">
        <svg class="contact-icon" viewBox="0 0 42 42" aria-hidden="true">
          <circle cx="21" cy="21" r="19" fill="#fff" stroke="var(--green)" stroke-width="2.5"/>
          <path d="M21 32c-5-7-8-10-8-14a8 8 0 0 1 16 0c0 4-3 7-8 14z" fill="var(--green)"/>
          <circle cx="21" cy="18" r="3" fill="#fff"/>
        </svg>
        <span class="contact-text">Unit 12, Harbour Row, LN4 7QP<br>48 Elm Street North</span>
      </li>
    </ul>
    <div class="holder">
      <p class="holder-name">MARA LINDEN</p>
      <p class="holder-role">Founder</p>
    </div>
  </div>
</section>

</body>
</html>
```